Electrical company business card design.

Hi, were an electrical company in Auckland New Zealand called Quarneth Ltd. We focus mainly on high end residential and commercial so the card would be targeted towards that.
The card will be for myself, i am the director of the company.
Name: Derek Olstow
Position: Director/electrician
Phone: 021 387 9415
Email: derek@quarneth.co.nz
Location: Auckland
As for colors the the blue color in the logo is preferred, i also don't mind a black background option.
Target Market(s)
High end residential and commercial
Industry/Entity Type
Electrician
Contact Information for Business Card
Name: Derek Olstow Position: Director/Electrician Phone: 021 387 9415, Email: derek@quarneth.co.nz, Location: Auckland

```html
<!DOCTYPE html>
<html lang="en">
<head>
<meta charset="utf-8">
<title>Quarneth Ltd – Business Card</title>
<link rel="stylesheet" href="https://fonts.googleapis.com/css2?family=Roboto:wght@300;400;500;700&display=swap">
<style>
  :root {
    --stage: #3a3a3c;
    --card: #161617;
    --card-light: #262628;
    --card-dark: #0d0d0e;
    --ink: #f2f2f2;
    --ink-soft: #c4c4c4;
    --rule: #d8d8d8;
    --blue: #1b7fd6;
    --blue-light: #2a9af0;
    --blue-deep: #0d55b0;
  }
  * { box-sizing: border-box; margin: 0; padding: 0; }
  html, body { width: 1200px; height: 694px; overflow: hidden; }
  body {
    background: var(--stage);
    font-family: "Roboto", Arial, sans-serif;
    position: relative;
  }
  .card {
    position: absolute;
    top: 197px;
    width: 520px;
    height: 300px;
    border-radius: 30px;
    background: var(--card);
    box-shadow: 0 12px 32px rgba(0,0,0,.5);
    overflow: hidden;
  }
  .card--back { left: 50px; }
  .card--front { left: 630px; }

  /* back */
  .brand-pattern {
    position: absolute; inset: 0;
    background:
      repeating-linear-gradient(135deg,
        var(--card-light) 0 22px,
        var(--card) 22px 44px);
    opacity: .9;
  }
  .brand {
    position: absolute;
    display: flex; align-items: center; gap: 8px;
    color: var(--ink);
    font-weight: 700;
    letter-spacing: .5px;
    white-space: nowrap;
  }
  .brand__mark {
    width: 14px; height: 14px;
    background: var(--blue);
  }
  .card--back .brand {
    right: 60px; top: 122px; font-size: 28px;
    padding: 4px 10px;
    background: var(--card-dark);
    border-radius: 4px;
  }
  .card--back .brand__mark { width: 22px; height: 22px; }

  /* front */
  .rule {
    position: absolute; left: 44px; right: 44px;
    height: 1px; background: var(--rule);
  }
  .rule--top { top: 44px; }
  .rule--mid { top: 186px; }
  .holder {
    position: absolute; left: 0; right: 0; top: 56px;
    text-align: center;
  }
  .holder__name {
    font-size: 32px; font-weight: 500; color: var(--ink);
    line-height: 1.1;
  }
  .holder__role {
    font-size: 9px; font-weight: 400; color: var(--ink-soft);
    letter-spacing: 3.5px; margin-top: 3px;
  }
  .phone {
    position: absolute; left: 58px; top: 122px;
  }
  .phone__label {
    display: flex; align-items: center; gap: 6px;
    font-size: 9px; letter-spacing: 3.5px; color: var(--ink-soft);
  }
  .phone__number {
    font-size: 40px; font-weight: 500; letter-spacing: .5px;
    background: linear-gradient(180deg, var(--blue-light), var(--blue-deep));
    -webkit-background-clip: text; background-clip: text;
    -webkit-text-fill-color: transparent;
    line-height: 1.05;
    white-space: nowrap;
  }
  .card--front .brand { right: 40px; top: 150px; font-size: 15px; }
  .city {
    position: absolute; left: 0; right: 0; top: 200px;
    display: flex; flex-direction: column; align-items: center; gap: 10px;
  }
  .city__landmark {
    width: 26px; height: 44px;
    background: linear-gradient(180deg, #e6e6e6, #8c8c8c);
    border-radius: 3px;
  }
  .city__name {
    font-size: 12px; letter-spacing: 6px; color: var(--ink);
    padding-left: 6px;
  }
</style>
</head>
<body>
  <section class="card card--back" aria-label="Card back">
    <div class="brand-pattern" role="img" aria-label="Embossed repeating brand name and tagline pattern in tone-on-tone black"></div>
    <div class="brand"><span class="brand__mark"></span>Quarneth</div>
  </section>

  <section class="card card--front" aria-label="Card front">
    <div class="rule rule--top"></div>
    <div class="holder">
      <p class="holder__name">Derek Olstow</p>
      <p class="holder__role">DIRECTOR/ELECTRICIAN</p>
    </div>
    <div class="phone">
      <p class="phone__label">
        <svg width="12" height="10" viewBox="0 0 12 10" aria-hidden="true">
          <path d="M1 4 Q6 0 11 4 L9.5 5.5 L8 4.5 L8 3.5 Q6 2.8 4 3.5 L4 4.5 L2.5 5.5 Z" fill="#e0e0e0"/>
          <rect x="3" y="6" width="6" height="3.5" rx="1" fill="#e0e0e0"/>
        </svg>
        PHONE
      </p>
      <p class="phone__number">021 387 9415</p>
    </div>
    <div class="brand"><span class="brand__mark"></span>Quarneth</div>
    <div class="rule rule--mid"></div>
    <div class="city">
      <div class="city__landmark" role="img" aria-label="Small line illustration of the Auckland Sky Tower"></div>
      <p class="city__name">AUCKLAND</p>
    </div>
  </section>
</body>
</html>
```